Design Large Inspirational Artwork with Long Quote

Design a large piece of art with a quote from Marcus Tillwright.

QUOTE
"The thing that's so interesting about being alive is that you're all in. No matter what you do, you're all in. This is gonna kill you, so I think you might as well play the most magnificent game you can while you're waiting. Because, do you have anything better to do? Why not pick the best thing possible that you could do? Because you're more powerful than you think, way more powerful than you think. I mean, God only knows what you are in the final analysis. You're blind to your own weaknesses, but you're also blind to your own strengths. How far could you take that if you stopped wasting time, and if you stopped lying, and if you oriented yourself to the highest possible good that you could conceive of and you committed to that? How much good could you do? Well, I would say: why don't you find out?"

SIZE
A high-resolution print size of 6' wide and 3' tall should provide ample space for both the quote and the accompanying artwork.

TYPOGRAPHY
Choose a bold, clean, and easily readable font for the quote. You could also experiment with different font sizes for certain words or phrases to emphasize their importance within the quote.

COLORS
Since the quote is thought-provoking and reflective, you might want to use a color palette that evokes a sense of introspection and depth. Consider using cool, calming colors like shades of blue, gray, or green. Alternatively, you can use a contrasting color scheme with a light background and dark text to make the quote stand out.

ARTWORK
Select / create / edit background artwork to complement the quote.
While a great design might be minimalistic and/or greyscale, I'd really like to see some full color options. This might be anything from photography or graphics inspired by the ideas in the text, to abstract colors or illustrations that feel like the sentiment expressed.
The art should capture your attention and encourage you to read the text. The art should be visually appealing, both at a distance and up close, regardless of whether the text is read.
Updates

Having trouble confirming the exact print size.

Still looking for printing solution and final size confirmation.

Target Market(s)

Personal, business, office

Industry/Entity Type

None

Font styles to use
Sans Serif
Script

Requirements
Must have
• Entire quote, legible text, modern design, attractive artwork, approx 6ft wide and 3ft tall
Nice to have
• Different font (sizes) for certain words or phrases to emphasize their importance within the quote.

```html
<!DOCTYPE html>
<html lang="en">
<head>
<meta charset="utf-8">
<title>All In — Quote Artwork</title>
<link rel="stylesheet" href="https://fonts.googleapis.com/css2?family=Roboto+Condensed:wght@300;700&family=Dancing+Script:wght@500&display=swap">
<style>
  :root {
    --page-bg: #ffffff;
    --art-bg: #ffffff;
    --text-soft: #4a4a4a;
    --text-strong: #111111;
    --quote-mark: #c4c4c4;
    --signature: #6e6e6e;
    --sky-light: #f2f2f2;
    --ridge-pale: #bdbdbd;
    --ridge-mid: #6e6e6e;
    --ridge-dark: #2e2e2e;
    --ridge-black: #0a0a0a;
  }
  * { margin: 0; padding: 0; box-sizing: border-box; }
  html, body {
    width: 1200px;
    height: 804px;
    overflow: hidden;
    background: var(--page-bg);
  }
  .artwork {
    position: absolute;
    left: 122px;
    top: 163px;
    width: 956px;
    height: 478px;
    background: var(--art-bg);
    overflow: hidden;
  }
  .landscape {
    position: absolute;
    left: 0;
    right: 0;
    bottom: 0;
    height: 150px;
    background:
      radial-gradient(ellipse 70px 45px at 591px 35px, rgba(255,255,255,0.95), rgba(255,255,255,0) 70%),
      linear-gradient(to bottom,
        rgba(242,242,242,0) 0%,
        var(--sky-light) 12%,
        var(--ridge-pale) 28%,
        var(--ridge-mid) 50%,
        var(--ridge-dark) 75%,
        var(--ridge-black) 100%);
  }
  .quote-mark {
    position: absolute;
    width: 39px;
    height: 43px;
  }
  .quote-mark--open { left: 57px; top: 51px; }
  .quote-mark--close { left: 859px; top: 281px; }
  .quote-mark path { fill: var(--quote-mark); }
  .quote {
    position: absolute;
    left: -8px;
    top: 68px;
    width: 956px;
    font-family: "Roboto Condensed", "Arial Narrow", sans-serif;
    font-weight: 300;
    font-size: 18.8px;
    line-height: 30.8px;
    color: var(--text-soft);
    text-align: center;
    white-space: nowrap;
  }
  .quote strong {
    font-weight: 700;
    color: var(--text-strong);
    font-size: 19.6px;
  }
  .quote .emphasis-lead {
    font-size: 24px;
  }
  .attribution {
    position: absolute;
    right: 111px;
    top: 318px;
    font-family: "Dancing Script", cursive;
    font-weight: 500;
    font-size: 22px;
    color: var(--signature);
  }
</style>
</head>
<body>
  <main class="artwork">
    <div class="landscape" role="img" aria-label="Black and white mountain range at sunrise, with a lone hiker standing hands on hips on a central rocky peak"></div>

    <svg class="quote-mark quote-mark--open" viewBox="0 0 39 43" aria-hidden="true">
      <path d="M0 0 H15 V10 L9 43 H0 Z"/>
      <path d="M24 0 H39 V10 L33 43 H24 Z"/>
    </svg>

    <blockquote class="quote">
      The thing that's so interesting about being alive is that you're <strong class="emphasis-lead">all in.</strong> No matter what you do, you're all<br>
      in. This is gonna kill you, so I think you might as well play the most magnificent game you can while<br>
      you're waiting. Because, do you have anything better to do? Why not pick the <strong>best thing possible</strong> that<br>
      you could do? Because you're more powerful than you think, way <strong>more powerful than you think.</strong><br>
      I mean, God only knows what you are in the final analysis. You're <strong>blind to your own weaknesses,</strong> but<br>
      you're also <strong>blind to your own strengths.</strong> How far could you take that if you stopped wasting time, and<br>
      if you stopped lying, and if you oriented yourself to the <strong>highest possible good</strong> that you could conceive<br>
      of and you committed to that? How much good could you do? Well, I would say: why don't you find out?
    </blockquote>

    <svg class="quote-mark quote-mark--close" viewBox="0 0 39 43" aria-hidden="true">
      <path d="M0 0 H15 V10 L9 43 H0 Z"/>
      <path d="M24 0 H39 V10 L33 43 H24 Z"/>
    </svg>

    <p class="attribution">- Marcus Tillwright -</p>
  </main>
</body>
</html>
```